Building technology company seek stationery design and folder design

Letterhead, and a folder design
ideally, I would have two letter head design, one is for one-page bussiness letter. the other one I can use for longer document such report, or analysis regular report page
you can find company logo and overall style at our website:
www.plinthcove.example

we are in building technology business, using internet of things technology to improve building energy efficiency to make building greener.

Industry/Entity Type

It Company

Requirements
Must have
• company logo
Nice to have
• techy look abstract graphics, etc.
Should not have
• no comment

```html
<!DOCTYPE html>
<html lang="en">
<head>
<meta charset="utf-8">
<title>Plinth Cove Folder</title>
<link rel="stylesheet" href="https://fonts.googleapis.com/css2?family=Open+Sans:wght@400;600&display=swap">
<style>
  :root {
    --stage-light: #f4f4f4;
    --stage-dark: #b9b9b9;
    --folder-ink: #061f21;
    --accent-green: #9bc53d;
    --skyline-grey: #858373;
    --text-light: #f2f2f2;
  }
  * { margin: 0; padding: 0; box-sizing: border-box; }
  html, body { width: 1200px; height: 847px; overflow: hidden; }
  body {
    background: radial-gradient(ellipse at 55% 30%, var(--stage-light) 0%, #dcdcdc 55%, var(--stage-dark) 100%);
    font-family: "Open Sans", sans-serif;
    position: relative;
  }
  .folder-spread {
    position: absolute;
    left: 110px; top: 110px;
    width: 980px; height: 620px;
    display: flex;
    box-shadow: 0 18px 40px rgba(0,0,0,0.25);
  }
  .panel {
    position: relative;
    width: 50%; height: 100%;
    background: var(--folder-ink);
    overflow: hidden;
  }
  .panel--back { border-right: 1px solid rgba(255,255,255,0.05); }
  .top-band {
    position: absolute; top: 0; left: 0; right: 0;
    height: 9px;
    background: var(--accent-green);
  }
  .base-band {
    position: absolute; bottom: 0; left: 0; right: 0;
    height: 24px;
    background: var(--skyline-grey);
  }
  .skyline {
    position: absolute; bottom: 24px;
    height: 26px;
    background: var(--skyline-grey);
  }
  .panel--back .skyline { left: 60px; width: 110px; }
  .panel--back .skyline--far { left: 340px; width: 110px; height: 20px; }
  .panel--front .skyline { left: 40px; width: 95px; height: 20px; }
  .panel--front .skyline--far { left: 300px; width: 100px; height: 22px; }
  .address {
    position: absolute; left: 140px; bottom: 72px;
    color: var(--text-light);
    font-size: 10px;
    letter-spacing: 0.2px;
  }
  .web-address {
    position: absolute; right: 90px; bottom: 70px;
    color: var(--text-light);
    font-size: 10px;
  }
  .brand {
    position: absolute; left: 90px; top: 190px;
    display: flex; align-items: center; gap: 12px;
  }
  .brand-mark {
    width: 26px; height: 26px;
    background: var(--accent-green);
  }
  .brand-name {
    color: var(--accent-green);
    font-size: 30px;
    font-weight: 400;
    letter-spacing: 2px;
    text-transform: uppercase;
  }
</style>
</head>
<body>
  <main class="folder-spread">
    <section class="panel panel--back">
      <div class="top-band"></div>
      <p class="address">48th Ave NW Suite 200, Oregon USA 97001</p>
      <div class="skyline" role="img" aria-label="City skyline silhouette"></div>
      <div class="skyline skyline--far" role="img" aria-label="City skyline silhouette"></div>
      <div class="base-band"></div>
    </section>
    <section class="panel panel--front">
      <div class="top-band"></div>
      <div class="brand">
        <span class="brand-mark"></span>
        <span class="brand-name">Plinth Cove</span>
      </div>
      <p class="web-address">www.plinthcove.example</p>
      <div class="skyline" role="img" aria-label="City skyline silhouette"></div>
      <div class="skyline skyline--far" role="img" aria-label="City skyline silhouette"></div>
      <div class="base-band"></div>
    </section>
  </main>
</body>
</html>
```